Flyer for Custom Home Builder!

my company is Harlow Ridge Homes, I am looking for a flyer that we can send via email to a customer, or print and hand out. I am thinking four pages so we could print this and fold it., possibly creating a folder. The name of the company is Harlow Ridge Homes our website is here www.harlowridgehomes-example.com. Some text you can use "Crafting luxury homes isn't just a job, it's our passion.
With meticulous attention to detail and an unwavering commitment to using the finest materials, Harlow Ridge Homes consistently delivers exceptional results that stand as a testament to our commitment to quality."

"Trust is the cornerstone of our foundation.
With a proven track record of delivering on our promises for over 16 years, we prioritize transparent communication and integrity throughout every step of the home-building journey".

you may need to obtain the photos here
https://files.example-share.net/f/k27pw4m8zrt03xq61bnv/h?key=48vn2c9q1x7mb5t0ekd3h&dl=0

Target Market(s)

We build homes for every wealthy clients, therefore the photos are extremely important

Industry/Entity Type

Construction.

Requirements
Must have
• clear larger photos

```html
<!DOCTYPE html>
<html lang="en">
<head>
<meta charset="utf-8">
<title>Harlow Ridge Homes – Flyer</title>
<link rel="stylesheet" href="https://fonts.googleapis.com/css2?family=Antonio:wght@700&family=Josefin+Sans:wght@400&display=swap">
<style>
  :root {
    --page-bg: #e6e6e6;
    --paper: #ffffff;
    --ink: #111111;
    --ink-soft: #3a3a3a;
    --brand-gray: #4a4a4a;
    --headline-gray: #a3a3a3;
    --tri-light: #d2d2d2;
    --tri-mid: #b9b9b9;
    --tri-dark: #a2a2a2;
    --tri-pale: #dedede;
    --wash: #f2f2f2;
  }
  * { margin: 0; padding: 0; box-sizing: border-box; }
  html, body { width: 1200px; height: 1200px; overflow: hidden; }
  body { background: var(--page-bg); position: relative; }

  .flyer {
    position: absolute; left: 234px; top: 82px;
    width: 732px; height: 1035px;
    background: var(--paper);
    overflow: hidden;
  }
  .interior-wash {
    position: absolute; left: 0; top: 606px; width: 732px; height: 429px;
    background: linear-gradient(180deg, #f7f7f7 0%, var(--wash) 60%, #ececec 100%);
  }
  .shapes { position: absolute; left: 0; top: 0; width: 732px; height: 1035px; }

  .photo { position: absolute; }
  .photo--pool {
    left: 0; top: 0; width: 732px; height: 1035px;
    clip-path: polygon(451px 110px, 732px 110px, 732px 604px, 450px 604px, 308px 356px);
    background: linear-gradient(180deg, #8fb6dc 10%, #9a8a76 30%, #50585c 48%, #c9c4bb 62%, #6fb5c4 80%, #3f8ea0 100%);
  }
  .photo--house {
    left: 0; top: 0; width: 732px; height: 1035px;
    clip-path: polygon(0 631px, 287px 631px, 340px 806px, 287px 981px, 0 981px);
    background: linear-gradient(180deg, #3d5f9a 0%, #7f8fb0 22%, #b9b6bf 38%, #9ea3a8 55%, #8a8e90 72%, #6e6c69 100%);
  }

  .brand {
    position: absolute; left: 50px; top: 66px;
    font-family: "Antonio", sans-serif; font-weight: 700;
    font-size: 30px; letter-spacing: 1.5px; line-height: 1;
    color: var(--brand-gray); white-space: nowrap;
  }

  .headline {
    position: absolute; left: 37px; top: 172px;
    font-family: "Antonio", sans-serif; font-weight: 700;
    text-transform: uppercase; white-space: nowrap;
  }
  .headline .line { display: block; }
  .headline .line-1 { font-size: 41px; line-height: 46px; color: var(--headline-gray); }
  .headline .line-2 { font-size: 29.5px; line-height: 36px; color: var(--ink); }
  .headline .line-3 { font-size: 41px; line-height: 48px; color: var(--ink); }
  .headline .accent { display: inline; color: var(--headline-gray); }

  .statement {
    position: absolute; right: 37px; top: 652px;
    font-family: "Josefin Sans", sans-serif; font-weight: 400;
    font-size: 20.5px; line-height: 26.3px; color: var(--ink);
    text-align: right; white-space: nowrap;
  }

  .contact {
    position: absolute; right: 28px; top: 940px;
    font-family: "Josefin Sans", sans-serif; font-size: 13.5px; line-height: 18px;
    color: var(--ink-soft); text-align: right; list-style: none;
  }
  .contact li { display: flex; justify-content: flex-end; align-items: flex-start; gap: 8px; }
  .contact .icon { width: 10px; height: 10px; margin-top: 3px; flex: none; }

  .website {
    position: absolute; left: 34px; top: 995px;
    display: flex; align-items: center; gap: 7px;
    font-family: "Josefin Sans", sans-serif; font-size: 13.5px; color: var(--ink-soft);
  }
  .website .icon { width: 11px; height: 11px; }
</style>
</head>
<body>
  <main class="flyer">
    <div class="interior-wash" role="img" aria-label="Faded photo of a bright luxury home interior"></div>

    <svg class="shapes" viewBox="0 0 732 1035" aria-hidden="true">
      <polygon points="0,519 250,627 287,631 0,631" fill="var(--tri-light)"/>
      <polygon points="37,312 289,365 250,627" fill="var(--tri-light)"/>
      <polygon points="289,365 250,627 138,444" fill="var(--tri-dark)"/>
      <polygon points="289,365 308,356 448,604 250,627" fill="var(--tri-mid)"/>
      <polygon points="250,627 448,604 340,806 287,631" fill="var(--tri-pale)"/>
      <polygon points="732,829 732,1035 388,1035" fill="var(--tri-mid)"/>
    </svg>

    <div class="photo photo--pool" role="img" aria-label="Photo of a modern luxury home patio with outdoor fireplace, lounge seating and a plunge pool"></div>
    <div class="photo photo--house" role="img" aria-label="Photo of a two-storey coastal custom home with wraparound porches at dusk"></div>

    <div class="brand">HARLOW RIDGE HOMES</div>

    <h1 class="headline">
      <span class="line line-1">Crafting Luxury</span>
      <span class="line line-2">Homes isn't just a job,</span>
      <span class="line line-3">It's <span class="accent">our passion</span></span>
    </h1>

    <p class="statement">Trust is the cornerstone of our<br>foundation.<br>With a proven track record of de-<br>livering on our promises for over<br>16 years, we prioritize transparent<br>communication and integrity<br>throughout every step of the<br>home-building journey</p>

    <ul class="contact">
      <li><span>555-014-2876</span>
        <svg class="icon" viewBox="0 0 10 10"><path d="M2 0.5l1.8 2-1 1.2a5.5 5.5 0 0 0 3.5 3.5l1.2-1 2 1.8-1.2 1.5C4.5 9.5 0.5 5.5 0.5 1.7Z" fill="currentColor"/></svg></li>
      <li><span>hello@harlowridge-example.com</span>
        <svg class="icon" viewBox="0 0 10 10"><rect x="0.5" y="2" width="9" height="6.5" rx="1" fill="currentColor"/><path d="M1 2.5l4 3 4-3" stroke="#fff" stroke-width="0.8" fill="none"/></svg></li>
      <li><span>48 Ridgeview Lane,<br>Suite 200, Austin TX 78700</span>
        <svg class="icon" viewBox="0 0 10 10"><path d="M5 0.5a3 3 0 0 0-3 3c0 2.2 3 6 3 6s3-3.8 3-6a3 3 0 0 0-3-3Z" fill="currentColor"/><circle cx="5" cy="3.5" r="1.1" fill="#fff"/></svg></li>
    </ul>

    <div class="website">
      <svg class="icon" viewBox="0 0 12 12"><circle cx="6" cy="6" r="5.3" fill="none" stroke="currentColor" stroke-width="1"/><ellipse cx="6" cy="6" rx="2.3" ry="5.3" fill="none" stroke="currentColor" stroke-width="0.9"/><path d="M0.8 6h10.4" stroke="currentColor" stroke-width="0.9"/></svg>
      <span>www.harlowridgehomes-example.com</span>
    </div>
  </main>
</body>
</html>
```